Gestaltung von Plakaten für Bereich der Qualitätssicherung
Zielgruppe
Wir sind Betreiber von zwei MERUFA Märkten.
Aufgabenstellung
Das Plakat dient zur internen Verwendung und soll anfallende Aufgaben im Bereich der Qualitätssicherung zeigen.
Es gibt die Marktleitung und 4 Abteilungen. In diesen 5 Bereichen fallen wiederkehrende Aufgaben in verschiedenen Zeitfenstern an.
Es soll herausstechen, dass die Marktleitung für die anderen 4 Abteilungen verantwortlich ist. (Organigramm)
Bitte fügen Sie zu jeden der 5 Zuständigkeitsbereiche eine freie Zeile hinzu. (Verantwortlich im Markt: __________)
Im Anhang habe ich eine Word Datei mit allen Abteilungen und deren Aufgaben und eine grobe Skizze hinzugefügt.
Überschrift des Plakats: Qualitätssicherung im Markt
Die Gestaltung soll einfach aber hochwertig wirken. Nicht verspielt. Weißer oder schlichter Hintergrund.
Das Ziel ist durch das Plakat eine Übersicht zu schaffen, wer für welche Aufgaben wann verantwortlich ist.
Wichtig ist das der Rhythmus (Wann muss es erledigt werden) am Plakat deutlich zu sehen ist.
Bitte fügen Sie das angehängte MERUFA Logo hinzu, dezent rechts unten im Eck.
In die Fußzeile bitte: BLT Abschlussprojekt von Jonas Kreibl, MERUFA Kreibl in Lindenhain
Wenn möglich bitte mit wenig kostenpflichtigen Stockmaterial.
Ich bin gespannt auf die Vorschläge.
Besten Dank im Voraus.

```html
<!DOCTYPE html>
<html lang="de">
<head>
<meta charset="utf-8">
<title>Qualitätssicherung im Markt</title>
<link href="https://fonts.googleapis.com/css2?family=Montserrat:wght@400;500;600;700&display=swap" rel="stylesheet">
<style>
  :root {
    --brand-blue: #17599f;
    --text-grey: #3a3a3a;
    --paper: #ffffff;
  }
  * { margin: 0; padding: 0; box-sizing: border-box; }
  html, body { width: 1200px; height: 801px; overflow: hidden; background: var(--paper); }
  body { font-family: "Montserrat", Arial, sans-serif; color: var(--text-grey); }
  .poster { position: relative; width: 1200px; height: 801px; }
  .abs { position: absolute; white-space: nowrap; }

  .poster-title { left: 50px; top: 42px; font-size: 46px; font-weight: 700; color: var(--brand-blue); letter-spacing: 0.2px; }

  .lead-box { left: 38px; top: 128px; width: 225px; height: 62px; background: var(--brand-blue); color: var(--paper);
    font-size: 27px; font-weight: 700; display: flex; align-items: center; justify-content: center; }

  .chart-lines { position: absolute; left: 0; top: 0; }

  .responsible-for { left: 99px; top: 273px; width: 100px; text-align: center; font-size: 15px; font-weight: 500;
    color: var(--brand-blue); line-height: 19px; }

  .rhythm { font-size: 16.5px; font-weight: 700; color: var(--brand-blue); left: 414px; }
  .task { font-size: 16.5px; font-weight: 400; color: var(--text-grey); left: 585px; }
  .task.bullet::before { content: "·"; font-weight: 700; margin-right: 8px; margin-left: -11px; }

  .dept-box { top: 421px; height: 55px; width: 256px; border: 1.5px solid var(--brand-blue);
    display: flex; align-items: center; justify-content: center; font-size: 27px; font-weight: 700; color: var(--brand-blue); }

  .dept-column { position: absolute; top: 498px; width: 250px; font-size: 16.5px; line-height: 21px; }
  .owner-line { display: flex; align-items: flex-end; gap: 10px; }
  .owner-line .blank { display: inline-block; width: 112px; border-bottom: 1px solid var(--text-grey); margin-bottom: 6px; }
  .interval { margin-top: 19px; font-weight: 700; color: var(--brand-blue); }
  .task-list { list-style: none; margin-top: 14px; }
  .task-list li { position: relative; padding-left: 19px; margin-bottom: 17px; }
  .task-list li::before { content: ""; position: absolute; left: 4px; top: 8px; width: 4px; height: 4px; background: var(--text-grey); }
  .plain-task { margin-top: 14px; }

  .footer-band { left: 0; top: 755px; width: 1200px; height: 46px; background: var(--brand-blue); }
  .footer-text { right: 100px; top: 768px; font-size: 14.5px; color: var(--paper); font-weight: 500; }
  .market-name { right: 16px; top: 768px; font-size: 14.5px; font-weight: 500; color: var(--paper); }
</style>
</head>
<body>
<div class="poster">
  <h1 class="abs poster-title">Qualitätssicherung im Markt</h1>

  <svg class="chart-lines" width="1200" height="801" viewBox="0 0 1200 801">
    <g fill="none" stroke="#17599f" stroke-width="2">
      <line x1="263" y1="160" x2="379" y2="160"/>
      <polyline points="392,124 379,124 379,370 392,370"/>
      <line x1="149" y1="190" x2="149" y2="270"/>
      <line x1="149" y1="316" x2="149" y2="394"/>
      <line x1="148" y1="394" x2="1072" y2="394"/>
      <line x1="149" y1="394" x2="149" y2="414"/>
      <line x1="466" y1="394" x2="466" y2="414"/>
      <line x1="773" y1="394" x2="773" y2="414"/>
      <line x1="1071" y1="394" x2="1071" y2="414"/>
      <line x1="312" y1="424" x2="312" y2="736" stroke-width="1.5"/>
      <line x1="617" y1="430" x2="617" y2="741" stroke-width="1.5"/>
      <line x1="916" y1="430" x2="916" y2="741" stroke-width="1.5"/>
    </g>
    <g fill="#17599f">
      <polygon points="145,413 153,413 149,421"/>
      <polygon points="462,413 470,413 466,421"/>
      <polygon points="769,413 777,413 773,421"/>
      <polygon points="1067,413 1075,413 1071,421"/>
    </g>
  </svg>

  <div class="abs lead-box">Marktleitung</div>
  <div class="abs responsible-for">verantwortlich<br>für</div>

  <div class="abs rhythm" style="top:130px">1x im Monat</div>
  <div class="abs task" style="top:130px">Temperaturkontrolle aller Truhen</div>
  <div class="abs rhythm" style="top:165px">1x im Quartal</div>
  <div class="abs task" style="top:166px">Marktbegehung</div>
  <div class="abs rhythm" style="top:201px">1x im Jahr</div>
  <div class="abs task bullet" style="top:201px">Hygieneschulung</div>
  <div class="abs task bullet" style="top:227px">Mitarbeiterbelehrung Infektionsschutzgesetz</div>
  <div class="abs task bullet" style="top:252px">Kontrolle GQB- Ware</div>
  <div class="abs rhythm" style="top:290px">Nach Bedarf</div>
  <div class="abs task bullet" style="top:290px">Dokumentation der Verantwortlichkeiten</div>
  <div class="abs task bullet" style="top:315px">Ablage Nachweisdokumente Schädlingsbekämpfung</div>
  <div class="abs task bullet" style="top:340px">Dokumentation und Ablage Warenrückruf</div>

  <div class="abs dept-box" style="left:29px">Obst &amp; Gemüse</div>
  <div class="abs dept-box" style="left:338px">MoPro</div>
  <div class="abs dept-box" style="left:642px">Tiefkühl</div>
  <div class="abs dept-box" style="left:931px">Lebensmittel</div>

  <section class="dept-column" style="left:40px">
    <div class="owner-line">Verantwortl.: <span class="blank"></span></div>
    <div class="interval">täglich:</div>
    <ul class="task-list">
      <li>Dokumentation<br>Wareneingangskontrolle</li>
      <li>Temperaturkontrolle<br>steckerfertige Truhen</li>
      <li>Kennzeichnung<br>„behandelte Ware“</li>
    </ul>
  </section>

  <section class="dept-column" style="left:348px">
    <div class="owner-line">Verantwortl.: <span class="blank"></span></div>
    <div class="interval" style="padding-left:9px">täglich:</div>
    <ul class="task-list">
      <li>Dokumentation<br>Wareneingangskontrolle</li>
      <li>Temperaturkontrolle<br>steckerfertige Truhen</li>
      <li>MHD- Qualitätskontrolle<br>während der Lagerung</li>
    </ul>
  </section>

  <section class="dept-column" style="left:652px">
    <div class="owner-line">Verantwortl.: <span class="blank"></span></div>
    <div class="interval">pro Lieferung:</div>
    <p class="plain-task">Dokumentation<br>Wareneingangskontrolle</p>
    <div class="interval" style="margin-top:22px">wöchentlich:</div>
    <p class="plain-task" style="margin-top:10px">MHD- Qualitätskontrolle<br>während der Lagerung</p>
  </section>

  <section class="dept-column" style="left:940px">
    <div class="owner-line">Verantwortl.: <span class="blank"></span></div>
    <div class="interval" style="padding-left:7px">wöchentlich:</div>
    <p class="plain-task" style="padding-left:7px">MHD- Qualitätskontrolle<br>während der Lagerung</p>
  </section>

  <div class="abs footer-band"></div>
  <div class="abs footer-text">BLT Abschlussprojekt 2021 von Jonas Kreibl, MERUFA Kreibl in Lindenhain</div>
  <div class="abs market-name">MERUFA</div>
</div>
</body>
</html>
```